EXTENDED Store hours to serve your healthcare needs

I'M LOOKING FOR A NICE FLYER THAT SHOWS THE FOLLOWING INFORMATION:

Logo
address
tel phone and fax
email address

Extending our hours to meet the growing healthcare needs of our community. Fast delivery service!

Monday - Thursday 10am-midnight
Friday 10am-4pm
Saturday - Motzei Shabbos till midnight
Sunday 10am-7pm

Target Market(s)

Community

Industry/Entity Type

Pharmacy

Requirements
Must have
• Extended hours
• personal care
• expert advice
• superior service
Nice to have
• Looking for no people pictures
• Eye popping design
• Classic modern clean design
Should not have
• store description is services
• And should not say Fiirst to open and last to close

```html
<!DOCTYPE html>
<html lang="en">
<head>
<meta charset="utf-8">
<title>Kessel Pharmacy – Extended Hours</title>
<link rel="stylesheet" href="https://fonts.googleapis.com/css2?family=Arimo:wght@400&display=swap">
<style>
  :root {
    --sky-deep: #3d9ccc;
    --sky-mid: #55c6f2;
    --sky-light: #8fdcfa;
    --ink: #111111;
    --brand-blue: #2c4fa0;
    --mint-top: #b3f4da;
    --mint-bottom: #7ce8b6;
    --band-top: #e6ecf7;
    --band-bottom: #c3dff3;
    --teal-strong: #48d0c8;
    --teal-soft: #a3dde0;
    --curve-black: #050505;
    --white: #ffffff;
  }
  * { margin: 0; padding: 0; box-sizing: border-box; }
  html, body { width: 846px; height: 1200px; overflow: hidden; background: var(--white); }
  .flyer {
    position: relative;
    width: 846px;
    height: 1200px;
    overflow: hidden;
    font-family: "Arimo", Arial, sans-serif;
    color: var(--ink);
    background: linear-gradient(180deg, var(--sky-deep) 0%, var(--sky-mid) 70%, var(--sky-light) 100%);
  }
  .backdrop { position: absolute; inset: 0; width: 846px; height: 1200px; }
  .brand {
    position: absolute;
    left: 24px;
    top: 26px;
    display: flex;
    align-items: flex-start;
    gap: 26px;
  }
  .brand-mark {
    width: 96px;
    height: 96px;
    background: var(--brand-blue);
    margin-top: 40px;
  }
  .brand-name {
    color: var(--brand-blue);
    font-weight: 400;
    line-height: 1;
  }
  .brand-name .line-main { display: block; font-size: 112px; letter-spacing: -2px; margin-left: 60px; }
  .brand-name .line-sub { display: block; font-size: 50px; letter-spacing: 10px; margin-left: 310px; margin-top: 20px; }
  .accent-bar {
    position: absolute;
    right: 0;
    height: 34px;
    border-radius: 4px 0 0 4px;
    background: linear-gradient(90deg, var(--teal-strong) 0%, var(--teal-soft) 45%, var(--teal-soft) 100%);
  }
  .accent-bar.one { top: 260px; left: 478px; }
  .accent-bar.two { top: 332px; left: 579px; }
  .accent-bar.three { top: 405px; left: 683px; }
  .panel {
    position: absolute;
    background: linear-gradient(180deg, var(--mint-top) 0%, var(--mint-bottom) 55%, var(--mint-bottom) 100%);
    border-radius: 3px;
    box-shadow: 1px 2px 3px rgba(0,0,0,0.35);
  }
  .contact { left: 0; top: 464px; width: 573px; height: 294px; }
  .contact .field { position: absolute; left: 10px; font-size: 28px; }
  .contact .address { top: 55px; }
  .contact .phone { top: 128px; }
  .contact .email { top: 211px; }
  .announcement {
    position: absolute;
    left: 0;
    top: 842px;
    width: 846px;
    height: 83px;
    background: linear-gradient(180deg, var(--band-top) 0%, var(--band-bottom) 100%);
    box-shadow: 0 2px 3px rgba(0,0,0,0.3);
    font-size: 31px;
    line-height: 38px;
    padding: 6px 0 0 4px;
    letter-spacing: -0.2px;
  }
  .announcement .indent { padding-left: 8px; }
  .hours { left: 0; top: 957px; width: 580px; height: 207px; padding: 20px 0 0 5px; }
  .hours li, .features li { list-style: none; white-space: nowrap; }
  .hours li { font-size: 31px; line-height: 38.5px; }
  .features { left: 608px; top: 957px; width: 238px; height: 207px; padding: 22px 0 0 12px; }
  .features li { font-size: 29px; line-height: 38.5px; letter-spacing: -1px; }
</style>
</head>
<body>
<main class="flyer">
  <svg class="backdrop" viewBox="0 0 846 1200" aria-hidden="true">
    <defs>
      <linearGradient id="curveShade" x1="0" y1="0" x2="0" y2="1">
        <stop offset="0" stop-color="#000" stop-opacity="0.35"/>
        <stop offset="1" stop-color="#000" stop-opacity="0"/>
      </linearGradient>
    </defs>
    <path d="M0,155 C170,380 480,560 846,575 L846,640 C520,600 300,520 0,300 Z" fill="url(#curveShade)"/>
    <path d="M0,0 L846,0 L846,568 C500,565 200,390 0,130 Z" fill="var(--curve-black)"/>
    <path d="M0,0 L846,0 L846,538 C500,540 220,380 0,110 Z" fill="var(--white)"/>
  </svg>

  <header class="brand">
    <span class="brand-mark" aria-hidden="true"></span>
    <h1 class="brand-name">
      <span class="line-main">Kessel</span>
      <span class="line-sub">PHARMACY</span>
    </h1>
  </header>

  <span class="accent-bar one"></span>
  <span class="accent-bar two"></span>
  <span class="accent-bar three"></span>

  <section class="panel contact">
    <p class="field address">address :</p>
    <p class="field phone">tel phone and fax :</p>
    <p class="field email">email address :</p>
  </section>

  <p class="announcement">Extending our hours to meet the growing healthcare needs<br><span class="indent">of our community. Fast delivery service!</span></p>

  <ul class="panel hours">
    <li>Monday - Thursday 10am-midnight</li>
    <li>Friday 10am-4pm</li>
    <li>Saturday - Motzei Shabbos till midnight</li>
    <li>Sunday 10am-7pm</li>
  </ul>

  <ul class="panel features">
    <li>- Extended hours</li>
    <li>- personal care</li>
    <li>- expert advice</li>
    <li>- superior service</li>
  </ul>
</main>
</body>
</html>
```